Harbourne Dental Care

I need a nice business card design that is double sided. This is for a dental surgery. I have already had a logo designed and just need the business card put together.

It needs to be in a format such that I can make new business cards if new dentists begin working for me. Hence I need to be able to change the text in order to have new names written on new cards.

The front will have the following text:

Dr Farid Osman
B. Med. Sci. QMTI B.Dent. Alb. Uni

The logo will appear somewhere on the front. This is attached.

In addition will be the following writing that also needs to appear on the front of the card, perhaps at the bottom on the left side will be:

Shop 42, 210-238 Fernlow Street, North Sydney, NSW, 2060

and at the bottom on the right side will be:
(02) 5550 8137
e: info@harbournedentalcare.com.au
www.harbournedentalcare.com.au

On the back of the card will be a section for a map to be drawn (I have uploaded a picture) and also a section written as follows:

"Your next appointment is: (a line needs to be here to write date and time)"

Also I need two lines for two appointments to be written.

Thanks for your efforts!

```html
<!DOCTYPE html>
<html lang="en">
<head>
<meta charset="utf-8">
<title>Harbourne Dental Care – Business Card</title>
<link href="https://fonts.googleapis.com/css2?family=Gentium+Book+Plus:wght@400;700&family=Open+Sans:wght@600;700&display=swap" rel="stylesheet">
<style>
  :root {
    --navy: #2f6296;
    --cyan: #37c5f3;
    --rule: #c9d3de;
    --paper: #ffffff;
    --backdrop: #e8e9eb;
    --map-a: #eef2f7;
    --map-b: #dfe7f0;
  }
  html, body {
    margin: 0;
    width: 1200px;
    height: 1000px;
    overflow: hidden;
    background: var(--backdrop);
  }
  .canvas { position: relative; width: 1200px; height: 1000px; }
  .card {
    position: absolute;
    width: 630px;
    height: 364px;
    background: var(--paper);
    box-shadow: 4px 5px 8px rgba(0,0,0,0.28);
    overflow: hidden;
  }
  .card--front { left: 190px; top: 113px; }
  .card--back { left: 380px; top: 523px; }

  .brand {
    position: absolute;
    left: 62px; top: 78px;
    width: 230px;
    text-align: center;
  }
  .brand__dot {
    display: block;
    width: 66px; height: 66px;
    margin: 0 auto 14px;
    border-radius: 50%;
    background: var(--cyan);
  }
  .brand__name {
    font-family: "Gentium Book Plus", serif;
    font-weight: 700;
    font-size: 27px;
    line-height: 1.05;
    color: var(--navy);
    margin: 0;
  }
  .dentist {
    position: absolute;
    left: 345px; top: 26px;
  }
  .dentist__name {
    font-family: "Gentium Book Plus", serif;
    font-weight: 700;
    font-size: 35px;
    color: var(--navy);
    margin: 0;
    line-height: 1.1;
  }
  .dentist__quals {
    font-family: "Open Sans", sans-serif;
    font-weight: 700;
    font-size: 11px;
    color: var(--cyan);
    margin: 1px 0 0 2px;
    letter-spacing: 0.2px;
  }
  .contact {
    position: absolute;
    left: 344px; top: 161px;
    margin: 0; padding: 0;
    list-style: none;
    font-family: "Gentium Book Plus", serif;
    font-size: 15.5px;
    color: var(--navy);
  }
  .contact__item {
    display: flex;
    align-items: center;
    height: 26px;
  }
  .contact__icon { width: 17px; height: 17px; margin-right: 7px; flex: none; }
  .wave { position: absolute; left: 0; bottom: 0; width: 630px; height: 112px; }
  .address {
    position: absolute;
    left: 0; right: 0; top: 316px;
    text-align: center;
    font-family: "Open Sans", sans-serif;
    font-weight: 700;
    font-size: 13.5px;
    color: var(--navy);
    margin: 0;
  }

  .map {
    position: absolute;
    left: 36px; top: 46px;
    width: 300px; height: 220px;
    background: linear-gradient(135deg, var(--map-a), var(--map-b));
  }
  .appointment__title {
    position: absolute;
    left: 362px; top: 44px;
    margin: 0;
    font-family: "Gentium Book Plus", serif;
    font-weight: 400;
    font-size: 19px;
    color: var(--navy);
    text-decoration: underline;
    text-underline-offset: 3px;
    text-decoration-thickness: 1px;
  }
  .appointment__line {
    position: absolute;
    height: 0;
    border-top: 1px solid var(--rule);
  }
</style>
</head>
<body>
<main class="canvas">

  <section class="card card--front" aria-label="Business card front">
    <div class="brand">
      <span class="brand__dot"></span>
      <p class="brand__name">Harbourne<br>Dental Care</p>
    </div>

    <div class="dentist">
      <h1 class="dentist__name">Dr Farid Osman</h1>
      <p class="dentist__quals">B. Med. Sci. QMTI B.Dent. Alb. Uni</p>
    </div>

    <ul class="contact">
      <li class="contact__item">
        <svg class="contact__icon" viewBox="0 0 20 20" aria-hidden="true">
          <circle cx="10" cy="10" r="10" fill="var(--cyan)"/>
          <path d="M7 5.2l1.6 2.6-1 1.1c.6 1.3 1.6 2.3 2.8 2.9l1.1-1 2.5 1.6-.8 1.9c-3.7-.3-6.8-3.4-7.1-7.2z" fill="#fff"/>
        </svg>
        (02) 5550 8137
      </li>
      <li class="contact__item">
        <svg class="contact__icon" viewBox="0 0 20 20" aria-hidden="true">
          <circle cx="10" cy="10" r="10" fill="var(--cyan)"/>
          <rect x="5" y="6.5" width="10" height="7" fill="#fff"/>
          <path d="M5 6.5l5 4 5-4" fill="none" stroke="var(--cyan)" stroke-width="1"/>
        </svg>
        info@harbournedentalcare.com.au
      </li>
      <li class="contact__item">
        <svg class="contact__icon" viewBox="0 0 20 20" aria-hidden="true">
          <circle cx="10" cy="10" r="10" fill="var(--cyan)"/>
          <g fill="none" stroke="#fff" stroke-width="1.1">
            <circle cx="10" cy="10" r="5.5"/>
            <ellipse cx="10" cy="10" rx="2.4" ry="5.5"/>
            <path d="M4.5 10h11M5.5 7.2h9M5.5 12.8h9"/>
          </g>
        </svg>
        www.harbournedentalcare.com.au
      </li>
    </ul>

    <svg class="wave" viewBox="0 0 630 112" preserveAspectRatio="none" aria-hidden="true">
      <path d="M0 4 C150 -8 260 20 360 36 C470 54 560 40 630 20 V112 H0 Z" fill="var(--cyan)"/>
    </svg>
    <p class="address">Shop 42, 210-238 Fernlow Street, North Sydney, 2060</p>
  </section>

  <section class="card card--back" aria-label="Business card back">
    <div class="map" role="img" aria-label="Street map showing the location of Harbourne Dental Care"></div>

    <h2 class="appointment__title">Your next appointment:</h2>
    <div class="appointment__line" style="left:358px; width:228px; top:132px;"></div>
    <div class="appointment__line" style="left:358px; width:228px; top:190px;"></div>
    <div class="appointment__line" style="left:358px; width:228px; top:249px;"></div>
    <div class="appointment__line" style="left:38px; width:548px; top:307px;"></div>
  </section>

</main>
</body>
</html>
```